Commercial wall and ceiling contractor needs website

Construction trade companies are notoriously behind the rest of the world when it comes to using current technology to run their businesses; we are not one of those companies. We are a walls and ceilings contractor using up to date communications technologies and applying them unlike any other in our trade. As simple as it sounds, and it really is that simple, it is still a new idea in the trade. We are moving our customers towards communicating with us through a single point of contact using text and email; we distribute information to the appropriate internal party on our end. We need a website that generally appears traditionally familiar to the visitor while also expresses a fresh new approach and edginess to the trade business.

Target Market(s)

General contractors looking to get a bit of background info before inviting us to bid on their projects. This is not a high traffic environment. Their subsequent site visits will be primarily for contact info.

Industry/Entity Type

Construction Company

Number of Pages Required

3 page

Font styles to use
Sans Serif

Requirements
Must have
• The file I uploaded named "kolsite.docx" does not have to appear on the site in the same manner in which appears in the document file; but the info contained within that document does need to be represented on the site.

```html
<!DOCTYPE html>
<html lang="en">
<head>
<meta charset="utf-8">
<title>Stratwell Walls &amp; Ceilings</title>
<link href="https://fonts.googleapis.com/css2?family=Lato:wght@400;700;900&display=swap" rel="stylesheet">
<style>
:root{
  --green:#1f5d3a;
  --gold:#a8772a;
  --ink:#333;
  --muted:#555;
  --grey-bg:#efefef;
  --white:#fff;
  --foot-text:#dfe8e2;
}
*{margin:0;padding:0;box-sizing:border-box}
html,body{width:1200px;height:3607px;overflow:hidden}
body{position:relative;font-family:'Lato',sans-serif;color:var(--ink);background:var(--white)}
.abs{position:absolute}
.btn{position:absolute;display:flex;align-items:center;justify-content:center;border-radius:24px;color:#fff;font-weight:700;font-size:15px;letter-spacing:.2px}
.btn.gold{background:var(--gold)}
.btn.green{background:var(--green)}
.body-text{font-size:14.5px;line-height:26px;color:var(--muted)}
.h2{font-weight:900;font-size:27px;color:var(--green);letter-spacing:-.2px}
.top-line{left:0;top:0;width:1200px;height:4px;background:var(--green)}
.phone-tab{left:905px;top:0;width:220px;height:45px;background:var(--green);border-radius:0 0 8px 8px;color:#fff;font-size:19px;font-weight:700;display:flex;align-items:center;justify-content:center;gap:14px}
.logo{display:flex;align-items:center;gap:10px;font-weight:900;font-size:22px;letter-spacing:2px}
.logo .mark{width:34px;height:34px;border:4px solid currentColor}
.nav{left:581px;top:86px;width:546px;display:flex;justify-content:space-between;font-size:13px;font-weight:700;color:#333}
.nav .active{color:var(--gold)}
.hero{left:0;top:133px;width:1200px;height:526px;background:linear-gradient(100deg,#d6d6d4 0%,#ececea 45%,#f4f4f2 100%)}
.hero-title{right:75px;top:305px;font-size:37px;font-weight:900;color:var(--gold);text-align:right}
.hero-sub{right:75px;top:353px;font-size:25px;font-weight:700;line-height:32px;color:#111;text-align:right}
.tile{position:absolute;width:205px;height:123px;background:var(--gold);border-radius:10px;color:#fff;display:flex;flex-direction:column;align-items:center;justify-content:center;gap:10px;font-weight:900;font-size:18px}
.wwd-photo{left:0;top:1037px;width:587px;height:358px;background:linear-gradient(135deg,#9a9c9e,#cfd0cf 55%,#b6b8b8)}
.wwd-panel{left:587px;top:1037px;width:613px;height:358px;background:var(--grey-bg)}
.center{text-align:center}
.infographic{position:absolute;border-radius:6px;background:linear-gradient(135deg,#eef3f6,#e2e8e6)}
.try-band{left:0;top:2350px;width:1200px;height:250px;background:linear-gradient(90deg,#a8772a 0%,#6d6a2e 45%,#1f5d3a 100%)}
.try{top:2385px;color:#fff;font-weight:900;display:flex;align-items:center}
.card{left:136px;top:2478px;width:928px;height:280px;background:#fff;box-shadow:0 3px 8px rgba(0,0,0,.18)}
.blog-img{position:absolute;top:2913px;width:331px;height:180px}
.blog-title{position:absolute;top:3107px;font-size:23px;font-weight:700;color:var(--gold)}
.blog-text{position:absolute;top:3143px;width:300px;font-size:13.5px;line-height:23px;color:#333}
.blog-text span{color:var(--gold)}
.sub-band{left:0;top:3277px;width:1200px;height:80px;background:var(--gold)}
.footer{left:0;top:3357px;width:1200px;height:250px;background:var(--green)}
.f-head{font-size:14px;font-weight:700;color:#fff}
.f-link{font-size:13px;color:var(--foot-text);line-height:27.5px}
.f-info{font-size:13px;line-height:20px;color:var(--foot-text)}
.social{position:absolute;top:3306px;width:22px;height:22px;border-radius:50%;background:#fff}
</style>
</head>
<body>
<div class="abs top-line"></div>
<div class="abs phone-tab">
  <svg width="16" height="16" viewBox="0 0 24 24"><path fill="#fff" d="M6.6 10.8a15 15 0 006.6 6.6l2.2-2.2c.3-.3.7-.4 1-.2 1.1.4 2.3.6 3.6.6.6 0 1 .4 1 1V20c0 .6-.4 1-1 1A17 17 0 013 4c0-.6.4-1 1-1h3.5c.6 0 1 .4 1 1 0 1.2.2 2.4.6 3.6.1.3 0 .7-.2 1z"/></svg>
  604-555-0182
</div>
<div class="abs logo" style="left:78px;top:62px;color:var(--gold)"><span class="mark"></span>STRATWELL</div>
<nav class="abs nav"><span class="active">HOME</span><span>ABOUT US</span><span>SERVICES</span><span>BLOG</span><span>TESTIMONIALS</span><span>CONTACT US</span></nav>

<div class="abs hero" role="img" aria-label="Photo of two workers in hard hats finishing a white ceiling and wall"></div>
<div class="abs hero-title">STRATWELL WALLS &amp; CEILINGS</div>
<div class="abs hero-sub">We are a Commercial wall and<br>ceiling contractor.</div>
<div class="btn green" style="left:987px;top:433px;width:139px;height:44px">READ MORE</div>

<div class="abs h2" style="left:75px;top:713px">WELCOME TO OUR WEBSITE</div>
<p class="abs body-text" style="left:74px;top:757px;width:598px">Lorem ipsum dolor sit amet, consectetur adipiscing elit. Duis nec ante eu libero dapibus hendrerit. Integer sed lacus sit amet ipsum pellentesque pulvinar. Vivamus pellentesque rutrum lectus, pharetra ultrices nulla. Aenean feugiat neque risus, ac laoreet libero cursus eget. Donec lobortis tincidunt dui, vitae ullamcorper ligula tempor et. Phasellus pulvinar consequat leo, quis interdum quam vestibulum quis. Maecenas luctus neque id eros porttitor, ut porttitor ex semper.</p>
<div class="btn gold" style="left:74px;top:934px;width:141px;height:42px">READ MORE</div>

<div class="tile" style="left:704px;top:719px">
  <svg width="48" height="40" viewBox="0 0 48 40" fill="none" stroke="#fff" stroke-width="3"><rect x="3" y="3" width="42" height="34"/><path d="M3 3l10 10h22l10-10M13 13v24M35 13v24"/></svg>FRAME</div>
<div class="tile" style="left:920px;top:719px">
  <svg width="72" height="40" viewBox="0 0 72 40" fill="none" stroke="#fff" stroke-width="2.5"><path d="M2 30l30 8 38-16-30-8z"/><path d="M2 24l30 8 38-16M2 18l30 8 38-16M2 12l30 8 38-16-30-8z"/></svg>BOARD</div>
<div class="tile" style="left:704px;top:853px">
  <svg width="60" height="40" viewBox="0 0 60 40" fill="none" stroke="#fff" stroke-width="3"><circle cx="40" cy="20" r="17"/><circle cx="40" cy="20" r="6"/><path d="M40 3H14L4 14l12 4 14-6"/></svg>TAPE</div>
<div class="tile" style="left:920px;top:853px">
  <svg width="40" height="44" viewBox="0 0 40 44" fill="none" stroke="#fff" stroke-width="3"><path d="M8 4v36h28M8 28l26-22M14 10l6 6"/></svg>TBAR</div>

<div class="abs wwd-photo" role="img" aria-label="Photo of a worker drilling into a ceiling frame"></div>
<div class="abs wwd-panel"></div>
<div class="abs h2" style="left:614px;top:1092px">WHAT WE DO</div>
<p class="abs body-text" style="left:614px;top:1133px;width:490px;line-height:28px">Lorem ipsum dolor sit amet, consectetur adipiscing elit. Duis nec ante eu libero dapibus hendrerit. Integer sed lacus sit amet ipsum pellentesque pulvinar. Vivamus pellentesque rutrum lectus, pharetra ultrices nulla. Aenean feugiat neque risus, ac laoreet libero cursus eget onec lobortis tincidunt dui, vitae ullamcorper ligula tempor et.</p>
<div class="btn gold" style="left:614px;top:1294px;width:140px;height:44px">READ MORE</div>

<div class="abs h2 center" style="left:0;top:1455px;width:1200px">WHY STRATWELL?</div>
<p class="abs body-text center" style="left:90px;top:1499px;width:1020px">Today's communication landscape is dramatically different than it was a mere ten years ago. We use our phones less and less for making calls. In fact, it is reported that 70% of direct communication is through text messaging, not phone calls; with text messaging increasing in use by %7,700 since 2008. No surprise here.</p>
<div class="btn gold" style="left:530px;top:1596px;width:140px;height:42px">READ MORE</div>

<div class="infographic" style="left:80px;top:1695px;width:500px;height:250px" role="img" aria-label="Infographic on texting speed and average response times"></div>
<p class="abs body-text" style="left:613px;top:1739px;width:515px;line-height:28px">The average length of a phone call has sharply decreased since 2006. That's because it's easier to swap a bunch of short messages than it is to interrupt each other's work at hand with a phone call. Furthermore, 99% of text messages are read while only 33% of voicemail messages are heard; 95% of text messages are read within 3 minutes and, on average, responded to within 90 seconds.</p>

<p class="abs body-text" style="left:74px;top:2046px;width:530px;line-height:28px">One of the many ways that Stratwell is bringing technology to its trade is through communication tools. A single point of contact gets you where you want to go. We distribute the text and email internally. Not only that, we share equal access to our communication points to hold each other accountable for their respective responsibilities. This flow of information is a more efficient, effective, and direct.</p>
<div class="infographic" style="left:636px;top:2010px;width:490px;height:250px" role="img" aria-label="Infographic on how adults, consumers and bosses view business texting"></div>

<div class="abs try-band"></div>
<div class="abs try" style="left:136px;font-size:40px">Try It!</div>
<div class="abs try" style="left:310px;top:2393px;font-size:28px;gap:28px">
  <svg width="24" height="24" viewBox="0 0 24 24"><path fill="#fff" d="M6.6 10.8a15 15 0 006.6 6.6l2.2-2.2c.3-.3.7-.4 1-.2 1.1.4 2.3.6 3.6.6.6 0 1 .4 1 1V20c0 .6-.4 1-1 1A17 17 0 013 4c0-.6.4-1 1-1h3.5c.6 0 1 .4 1 1 0 1.2.2 2.4.6 3.6.1.3 0 .7-.2 1z"/></svg>604-555-0182</div>
<div class="abs try" style="left:596px;top:2396px;font-size:23px;gap:30px">
  <svg width="26" height="20" viewBox="0 0 26 20"><rect width="26" height="20" rx="2" fill="#fff"/><path d="M1 2l12 9 12-9" fill="none" stroke="#4a6a34" stroke-width="2"/></svg>hello@stratwellinteriors.com</div>

<div class="abs card"></div>
<svg class="abs" style="left:165px;top:2512px" width="56" height="34" viewBox="0 0 56 34"><path d="M0 34V16C0 6 6 0 16 0v8c-5 0-7 3-7 8h7v18zM30 34V16c0-10 6-16 16-16v8c-5 0-7 3-7 8h7v18z" fill="#e6e6e6"/></svg>
<svg class="abs" style="left:968px;top:2680px" width="56" height="34" viewBox="0 0 56 34"><path d="M26 0v18c0 10-6 16-16 16v-8c5 0 7-3 7-8h-7V0zM56 0v18c0 10-6 16-16 16v-8c5 0 7-3 7-8h-7V0z" fill="#e6e6e6"/></svg>
<div class="abs h2 center" style="left:136px;top:2527px;width:928px">WHAT OUR CLIENT SAYS</div>
<p class="abs center" style="left:215px;top:2577px;width:770px;font-size:14px;line-height:25px;color:#444">Lanventore veritatis et quasi architecto beatae vitae dicta sunt explicabo. Nemo enim ipsam voluptatem quia voluptas sit aspernatur aut odit aut fugit, sed quia consequuntur magni dolores eos qui ratione voluptatem sequi nesciunt. Neque porro quisquam est, qui dolorem ipsum quia dolor sit amet..."</p>
<div class="abs center" style="left:136px;top:2672px;width:928px;font-size:16px;font-weight:700;color:var(--gold)">-Name Heading</div>
<div class="abs center" style="left:136px;top:2699px;width:928px;font-size:11px;color:#444">Location</div>
<svg class="abs" style="left:164px;top:2600px" width="16" height="30"><path d="M14 2L3 15l11 13" fill="none" stroke="#666" stroke-width="2"/></svg>
<svg class="abs" style="left:1024px;top:2600px" width="16" height="30"><path d="M2 2l11 13L2 28" fill="none" stroke="#666" stroke-width="2"/></svg>

<div class="abs h2" style="left:73px;top:2842px">BLOG POSTS</div>
<svg class="abs" style="left:1082px;top:2842px" width="46" height="30"><path d="M12 3L2 15l10 12M34 3l10 12-10 12" fill="none" stroke="#666" stroke-width="2"/></svg>
<div class="blog-img" style="left:74px;background:linear-gradient(120deg,#e9e9e6,#a9aaa8)" role="img" aria-label="Photo of a worker painting a wall with a roller"></div>
<div class="blog-img" style="left:435px;background:linear-gradient(120deg,#ecebe8,#8d96a8)" role="img" aria-label="Photo of two workers plastering a ceiling"></div>
<div class="blog-img" style="left:795px;background:linear-gradient(120deg,#9a9c9e,#cfd0cf)" role="img" aria-label="Photo of a worker drilling into a ceiling frame"></div>
<div class="blog-title" style="left:74px">Inventore Veritatis</div>
<div class="blog-title" style="left:435px">Inventore Veritatis</div>
<div class="blog-title" style="left:795px">Inventore Veritatis</div>
<p class="blog-text" style="left:74px">Lanventore veritatis et quasi architecto beatae vitae dicta sunt explicabo. Nemo enim ipsam voluptatem quia ..<span>Read More</span></p>
<p class="blog-text" style="left:435px">Lanventore veritatis et quasi architecto beatae vitae dicta sunt explicabo. Nemo enim ipsam voluptatem quia ..<span>Read More</span></p>
<p class="blog-text" style="left:795px">Lanventore veritatis et quasi architecto beatae vitae dicta sunt explicabo. Nemo enim ipsam voluptatem quia ..<span>Read More</span></p>

<div class="abs sub-band"></div>
<div class="abs" style="left:76px;top:3306px;font-size:19px;font-weight:900;color:#fff">SUBSCRIBE EMAIL</div>
<div class="abs" style="left:255px;top:3298px;width:255px;height:38px;background:#fff;border-radius:2px;font-size:11px;font-weight:700;color:#333;padding:12px 10px">Enter Email Address</div>
<div class="abs" style="left:519px;top:3298px;width:101px;height:38px;background:#2b2b2b;border-radius:2px;font-size:11px;font-weight:700;color:#fff;display:flex;align-items:center;justify-content:center">SUBSCRIBE</div>
<div class="abs" style="left:794px;top:3306px;font-size:19px;font-weight:900;color:#fff">FOLLOW US</div>
<span class="social" style="left:916px"></span><span class="social" style="left:959px"></span><span class="social" style="left:1006px"></span><span class="social" style="left:1055px"></span><span class="social" style="left:1103px"></span>

<div class="abs footer"></div>
<div class="abs logo" style="left:78px;top:3430px;color:#fff"><span class="mark"></span>STRATWELL</div>
<div class="abs" style="left:76px;top:3506px;font-size:12px;line-height:23px;color:var(--foot-text)">Copyright © 2019, Company Name<br>All Right reserved</div>
<div class="abs f-head" style="left:351px;top:3400px">QUICK LINKS</div>
<div class="abs f-link" style="left:351px;top:3423px">Home<br>About Us<br>Services<br>Blog</div>
<div class="abs f-link" style="left:482px;top:3423px">Blog<br>Testimonials<br>Contact Us</div>
<div class="abs f-head" style="left:653px;top:3400px">RESOURCES</div>
<div class="abs f-link" style="left:653px;top:3423px">Cepteur sint<br>Lccaecat cupidatat<br>Non proident, sunt<br>Culpa qui officia deserunt</div>
<div class="abs f-head" style="left:907px;top:3400px">CONTACT INFO</div>
<svg class="abs" style="left:907px;top:3436px" width="14" height="20" viewBox="0 0 12 16" fill="#dfe8e2"><path d="M6 0a5 5 0 00-5 5c0 4 5 9 5 9s5-5 5-9a5 5 0 00-5-5zm0 7a2 2 0 110-4 2 2 0 010 4z"/></svg>
<svg class="abs" style="left:907px;top:3488px" width="13" height="13" viewBox="0 0 24 24"><path fill="#dfe8e2" d="M6.6 10.8a15 15 0 006.6 6.6l2.2-2.2c.3-.3.7-.4 1-.2 1.1.4 2.3.6 3.6.6.6 0 1 .4 1 1V20c0 .6-.4 1-1 1A17 17 0 013 4c0-.6.4-1 1-1h3.5c.6 0 1 .4 1 1 0 1.2.2 2.4.6 3.6.1.3 0 .7-.2 1z"/></svg>
<svg class="abs" style="left:907px;top:3521px" width="13" height="10" viewBox="0 0 26 20"><rect width="26" height="20" rx="2" fill="#dfe8e2"/><path d="M1 2l12 9 12-9" fill="none" stroke="#1f5d3a" stroke-width="2"/></svg>
<div class="abs f-info" style="left:940px;top:3433px">14 Birch Lane, Suite 2,<br>Portland, USA</div>
<div class="abs f-info" style="left:940px;top:3484px">1-800-555-0147</div>
<div class="abs f-info" style="left:940px;top:3516px">info@stratwellinteriors.com</div>
</body>
</html>
```